Waterjet manufacturing company needs brochure design

We need a brochure that outlines why waterjet manufacturing is beneficial for a variety of industries, our capabilities, core competencies and competitive advantages (see attached documents). The design should include our logo and include the same colours. (Dark blue RGB – 2,86,162, Light Blue RGB – 0,146,201). The design should be very clean, professional and eye catching. I've attached a few photos that can be used. Regarding the photo of the robot, please make the background white.

Manufacturing, construction, aerospace, home building

• - exact Logo colours included in design (see description)
• - booklet style design (not tri-fold)
• - professional looking
• - Logo on front cover with writing underneath:
• High Quality
• Tight Tolerance
• Components
• - Plankrow, Ropelane, Vidstow and Pixelmorra icons in Contact Us section

```html
<!DOCTYPE html>
<html lang="en">
<head>
<meta charset="utf-8">
<title>Tidecut Waterjet Brochure</title>
<link href="https://fonts.googleapis.com/css2?family=Montserrat:wght@400;600;800&family=Open+Sans:wght@400;600&display=swap" rel="stylesheet">
<style>
:root{
  --navy:#0256a2;
  --sky:#0092c9;
  --ink:#0a1f4a;
  --deep:#06142f;
  --paper:#ffffff;
  --page-grey:#e9ebee;
  --bg:#e4e4e4;
  --text:#3a4250;
}
*{box-sizing:border-box;margin:0;padding:0}
html,body{width:1200px;height:2384px;overflow:hidden;background:var(--bg)}
body{position:relative;font-family:"Open Sans",Arial,sans-serif;color:var(--text)}
.spread{position:absolute;left:50px;width:1100px;height:500px;display:flex;box-shadow:0 10px 24px rgba(0,0,0,.18)}
.page{position:relative;width:550px;height:500px;overflow:hidden}
.page + .page{border-left:1px solid rgba(0,0,0,.15)}
.photo{position:absolute}
.brand{font-family:"Montserrat",Arial,sans-serif;font-weight:800;color:var(--sky);letter-spacing:.5px;display:flex;align-items:center;gap:10px}
.brand .dot{width:22px;height:22px;background:var(--sky);border-radius:50%}
h2,h3,h4{font-family:"Montserrat",Arial,sans-serif;color:#fff}
p{font-size:11px;line-height:1.6}
.rivet{position:absolute;width:10px;height:10px;border-radius:50%;background:#c8d3dd;border:2px solid #7d8a96}
/* cover */
.back-cover{background:var(--page-grey)}
.front-cover{background:var(--paper)}
.contact-box{position:absolute;left:40px;top:250px;width:300px;height:120px;background:var(--navy);padding:22px;color:#fff}
.contact-box h4{font-size:15px;margin-bottom:8px}
.contact-box p{color:#cfe6f5}
.tagline{position:absolute;right:0;top:150px;width:250px;background:var(--navy);padding:16px 20px;text-align:right}
.tagline span{display:block;font-family:"Montserrat",sans-serif;font-weight:800;color:#fff;font-size:18px;line-height:1.3}
.cover-band{position:absolute;left:0;bottom:0;width:550px;height:110px}
.cover-label{position:absolute;right:24px;bottom:26px;font-family:"Montserrat",sans-serif;font-weight:600;color:#fff;font-size:12px;letter-spacing:2px;border:1px solid #fff;padding:6px 12px}
/* text panels */
.panel{position:absolute;background:rgba(2,86,162,.92);padding:24px;color:#dbeaf6}
.panel h3{font-size:16px;margin-bottom:10px}
.panel p{color:#dbeaf6}
/* list */
.service-list{list-style:none;margin-top:8px}
.service-list li{font-size:11.5px;color:#fff;padding:7px 0;border-bottom:1px solid rgba(255,255,255,.25)}
/* table */
.spec-table{width:100%;border-collapse:collapse;font-size:10.5px;color:#e3effa}
.spec-table th{background:var(--sky);color:#fff;font-family:"Montserrat",sans-serif;font-weight:600;text-align:left;padding:6px 8px}
.spec-table td{padding:6px 8px;border-bottom:1px solid rgba(255,255,255,.15)}
.spec-table tr:nth-child(even) td{background:rgba(255,255,255,.05)}
/* back pages */
.info-page{background:var(--paper);padding:36px 32px;display:grid;grid-template-columns:1fr 1fr;gap:20px 26px;align-content:start}
.info-page h4{color:var(--navy);font-size:13px;margin-bottom:6px}
.info-page p{color:#555d68;font-size:10.5px}
.contact-page{background:var(--paper)}
.contact-list{position:absolute;left:40px;top:36px}
.contact-list h4{color:var(--navy);font-size:15px;margin-bottom:12px}
.contact-row{display:flex;align-items:center;gap:10px;font-size:11.5px;color:#444;margin-bottom:8px}
.contact-row .chip{width:16px;height:16px;border-radius:50%;background:var(--navy)}
.contact-row svg{width:16px;height:16px}
</style>
</head>
<body>

<!-- Spread 1: covers -->
<section class="spread" style="top:60px">
  <div class="page back-cover">
    <div class="photo" role="img" aria-label="Light grey photo of a waterjet cutting head over machined parts" style="inset:0;background:linear-gradient(135deg,#f1f3f5 0%,#c9ced4 55%,#e6e9ec 100%);opacity:.9"></div>
    <div class="brand" style="position:absolute;left:40px;top:60px;font-size:52px"><span class="dot"></span>Tidecut</div>
    <div class="contact-box">
      <h4>Precision Waterjet Cutting</h4>
      <p>(555) 014-2280<br>info@tidecut.example<br>www.tidecut.example</p>
    </div>
  </div>
  <div class="page front-cover">
    <div class="photo" role="img" aria-label="Photo of a waterjet nozzle cutting a metal sheet with spray" style="left:0;top:0;width:550px;height:390px;background:linear-gradient(160deg,#dfe8ef 0%,#8fa6b8 45%,#2c4f72 100%)"></div>
    <div style="position:absolute;left:40px;top:40px;background:#fff;padding:12px 18px">
      <div class="brand" style="font-size:34px;color:var(--navy)"><span class="dot" style="background:var(--navy)"></span>Tidecut</div>
    </div>
    <div class="tagline"><span>High Quality</span><span>Tight Tolerance</span><span>Components</span></div>
    <svg class="cover-band" viewBox="0 0 550 110" preserveAspectRatio="none">
      <polygon points="0,30 550,0 550,110 0,110" fill="var(--navy)"/>
      <polygon points="0,30 550,0 550,14 0,44" fill="var(--sky)"/>
    </svg>
    <div class="cover-label">WATERJET SOLUTIONS</div>
  </div>
</section>

<!-- Spread 2: why waterjet -->
<section class="spread" style="top:636px">
  <div class="page" style="background:var(--deep)">
    <div class="photo" role="img" aria-label="Photo of a waterjet machine cutting head in blue light" style="inset:0;background:linear-gradient(140deg,#b9c7d6 0%,#4c6a8c 40%,#0d2345 100%)"></div>
    <div class="panel" style="left:0;bottom:0;width:550px;height:190px;background:linear-gradient(90deg,#0a2a5c,rgba(2,86,162,.95))">
      <h3>Why Waterjet Cutting</h3>
      <p>Abrasive waterjet cutting shapes metal, stone, glass and composites with a cold stream that leaves no heat zone, no warping and a clean edge ready for assembly, saving time on secondary finishing for every production run.</p>
    </div>
    <span class="rivet" style="left:16px;top:16px"></span><span class="rivet" style="right:16px;top:16px"></span>
  </div>
  <div class="page" style="background:var(--ink)">
    <div class="photo" role="img" aria-label="Photo of rippling water surface in bright blue" style="left:230px;top:0;width:320px;height:500px;background:linear-gradient(160deg,#5fc3e8 0%,#1d7fb8 50%,#0b3b73 100%)"></div>
    <svg style="position:absolute;left:0;top:0" width="550" height="500"><polygon points="0,0 300,0 250,500 0,500" fill="#0c2f66"/><line x1="300" y1="0" x2="250" y2="500" stroke="var(--sky)" stroke-width="3"/></svg>
    <div class="panel" style="left:24px;top:280px;width:260px;background:none;padding:0">
      <p>Our experienced team pairs modern five axis machines with careful inspection to deliver parts that hold tight tolerances from first prototype to full production, serving manufacturing, construction, aerospace and home building clients.</p>
    </div>
    <span class="rivet" style="right:16px;bottom:16px"></span>
  </div>
</section>

<!-- Spread 3: capabilities -->
<section class="spread" style="top:1212px">
  <div class="page" style="background:var(--navy)">
    <div class="photo" role="img" aria-label="Photo of a waterjet stream cutting through metal under blue light" style="inset:0;background:linear-gradient(130deg,#1a3f9a 0%,#0256a2 45%,#0092c9 75%,#0a2a5c 100%)"></div>
    <div class="panel" style="left:24px;top:24px;width:280px;background:rgba(6,20,47,.55)">
      <h3>Industries We Serve</h3>
      <ul class="service-list">
        <li>Manufacturing – brackets, plates and fixtures</li>
        <li>Construction – structural and architectural parts</li>
        <li>Aerospace – lightweight alloy and composite parts</li>
        <li>Home Building – stone, tile and glass inlays</li>
      </ul>
      <p style="margin-top:10px">Every job is programmed, cut and checked in house for fast turnaround.</p>
    </div>
  </div>
  <div class="page" style="background:var(--deep)">
    <svg style="position:absolute;left:0;top:0" width="550" height="500"><rect x="0" y="330" width="550" height="60" fill="var(--sky)" opacity=".35"/><rect x="0" y="390" width="550" height="110" fill="#0b2a5a"/></svg>
    <div style="position:absolute;left:24px;top:24px;width:500px">
      <h3 style="font-size:15px;margin-bottom:10px">Core Competencies &amp; Capabilities</h3>
      <table class="spec-table">
        <tr><th>Material</th><th>Thickness</th><th>Tolerance</th><th>Use</th></tr>
        <tr><td>Steel</td><td>150 mm</td><td>±0.1 mm</td><td>Frames</td></tr>
        <tr><td>Aluminium</td><td>200 mm</td><td>±0.1 mm</td><td>Panels</td></tr>
        <tr><td>Titanium</td><td>120 mm</td><td>±0.08 mm</td><td>Aerospace</td></tr>
        <tr><td>Stone</td><td>100 mm</td><td>±0.2 mm</td><td>Counters</td></tr>
        <tr><td>Glass</td><td>60 mm</td><td>±0.2 mm</td><td>Inlays</td></tr>
      </table>
      <h3 style="font-size:13px;margin:64px 0 8px">Competitive Advantages</h3>
      <table class="spec-table">
        <tr><td>No heat zone</td><td>Any shape</td><td>Low waste</td></tr>
      </table>
    </div>
  </div>
</section>

<!-- Spread 4: about and contact -->
<section class="spread" style="top:1788px">
  <div class="page info-page">
    <div><h4>About Us</h4><p>Tidecut is a family run cutting shop supplying accurate waterjet parts to builders and manufacturers, with skilled operators who treat every order, large or small, with the same care.</p></div>
    <div><h4>Quality</h4><p>Each part is measured against drawing before shipping, and our process keeps edges smooth and dimensions consistent across the whole batch.</p></div>
    <div><h4>Our Process</h4><p>Send a drawing or sample, receive a quote within a day, then approve a first article before we cut the full order.</p></div>
    <div><h4>Advantages</h4><p>Cold cutting, minimal kerf and flexible nesting keep material costs down and lead times short.</p></div>
  </div>
  <div class="page contact-page">
    <div class="contact-list">
      <h4>Contact Us</h4>
      <div class="contact-row"><span class="chip"></span>Plankrow</div>
      <div class="contact-row"><span class="chip"></span>Ropelane</div>
      <div class="contact-row"><span class="chip"></span>Vidstow</div>
      <div class="contact-row"><span class="chip"></span>Pixelmorra</div>
      <div class="contact-row"><svg viewBox="0 0 16 16"><path d="M4 1h3l1 4-2 1a8 8 0 0 0 4 4l1-2 4 1v3a2 2 0 0 1-2 2A13 13 0 0 1 2 3a2 2 0 0 1 2-2z" fill="var(--navy)"/></svg>(555) 014-2280</div>
      <div class="contact-row"><svg viewBox="0 0 16 16"><path d="M8 1a5 5 0 0 1 5 5c0 4-5 9-5 9S3 10 3 6a5 5 0 0 1 5-5z" fill="var(--navy)"/><circle cx="8" cy="6" r="2" fill="#fff"/></svg>42 Harbor Road, Millbrook</div>
    </div>
    <div class="photo" role="img" aria-label="Photo of a waterjet cutting head spraying water over a cut metal plate" style="left:250px;top:0;width:300px;height:500px;background:linear-gradient(170deg,#f0f2f4 0%,#a9b4bf 40%,#5d6b78 75%,#3b4650 100%)"></div>
  </div>
</section>

</body>
</html>
```